Brill's Jewelers website (www.brillsjewelers-example.com)

We are in need of a web storefront for a retail Jewelry store.
www.brillsjewelers-example.com
https://www.facebook.com/Brills-Jewelers-Palm-Vista-740315928461257/

Brill's Jewelers is located in Coral Gables, Florida. The store has been family owned and operated since 1958. Their focus customers are high-income families that care about quality over the brand name. They mostly sell fashion jewelry and diamonds up to 8 carats. We are looking for a simple minimalistic site that their customers can view their inventory and purchase items online.

Competitors websites:
https://www.orvinjewelers-example.com/
http://www.pelvaro-example.com/
http://truecutjewelers-example.com/

Pages:
-Home (with message bulletin)
-Jewelry
We would be able to create the subpages ie Rings, Bracelets, Earrings, Necklaces, Estate, Watches, Men's, Children's
-Services
We would need sub pages ie Appraisals, Consignment, Repairs
-About us
-Contact

Target Market(s)

Local wealthy families

Coding

Number of Pages Required

Font styles to use
Serif

Requirements
Must have
• -An E-commerce site customers can buy jewelry online.
-An easy process internally to add new items to the site
-Colors are Black and White or Black and Gold
Nice to have
• I would like to stay away from face shots of random models in stock photos. I want the jewelry pieces as the focus, not models.

```html
<!DOCTYPE html>
<html lang="en">
<head>
<meta charset="utf-8">
<title>Brill's Jewelers — Your Hometown Jeweler</title>
<link rel="stylesheet" href="https://fonts.googleapis.com/css2?family=Limelight&family=Josefin+Sans:wght@300;400;600;700&family=Cormorant+Garamond:wght@500&display=swap">
<style>
:root{
  --gold:#d6962b;
  --ink:#2a2a2a;
  --panel:#231f1f;
  --soft:#f2f2f2;
  --line:#d8d8d8;
  --white:#ffffff;
  --muted:#6b6b6b;
}
*{margin:0;padding:0;box-sizing:border-box}
html,body{width:1200px;height:4831px;overflow:hidden;background:var(--white)}
body{position:relative;font-family:"Josefin Sans",sans-serif;color:var(--ink)}
.abs{position:absolute}
section,header,footer{position:absolute;left:0;width:1200px}
.photo{position:absolute}
.deco{font-family:"Limelight",serif;letter-spacing:1px}
.name-mark{font-family:"Josefin Sans",sans-serif;font-weight:700;letter-spacing:1px}

/* header + hero */
.hero{top:0;height:643px;background:linear-gradient(120deg,#b9b2ad 0%,#8f8782 35%,#7b726e 60%,#a49c97 100%)}
.brand{left:84px;top:22px;color:var(--white)}
.brand .name{font-size:40px;line-height:1}
.brand .tag{font-size:12px;letter-spacing:1px;margin-top:8px}
.nav{left:420px;top:53px;display:flex;gap:27px;font-size:11px;letter-spacing:.5px;color:var(--white)}
.nav .active{color:var(--gold)}
.cart{left:1010px;top:43px;width:111px;height:32px;background:var(--gold);color:var(--white);font-size:11px;display:flex;align-items:center;justify-content:center;gap:6px}
.hero-title{left:150px;top:290px;color:var(--white);font-size:46px;line-height:54px;font-weight:400}
.hero-link{left:150px;top:428px;width:130px;color:var(--white);font-size:11px;letter-spacing:1px;padding:8px 0 8px 28px;border-top:1px solid rgba(255,255,255,.6);border-bottom:1px solid rgba(255,255,255,.6)}
.dots{left:1039px;top:325px;display:flex;flex-direction:column;gap:6px}
.dots i{width:6px;height:6px;border:1px solid var(--white);border-radius:50%}

/* services */
.services{top:643px;height:332px;background:var(--soft)}
.sec-title{width:1200px;left:0;text-align:center;font-size:26px;font-weight:300;letter-spacing:1px}
.svc{width:240px;text-align:center}
.svc svg{display:block;margin:0 auto}
.svc .rule{height:1px;background:var(--line);margin:16px 0 14px}
.svc p{font-size:17px}

/* shop grid */
.tile{width:205px;height:160px}
.tile-label{width:205px;text-align:center;font-size:16px}
.tile-label span{display:block;width:130px;height:1px;background:var(--line);margin:12px auto 0}
.tile-label.on{color:var(--gold)}

/* banner */
.banner{top:1663px;height:403px;background:linear-gradient(100deg,#9c9c9e 0%,#c4c4c6 45%,#8b8b8d 100%)}
.banner-title{left:154px;top:1787px;color:var(--white);font-size:42px;line-height:56px;font-weight:400}
.banner-title .thin{font-family:"Josefin Sans",sans-serif;font-weight:300}
.btn-gold{background:var(--gold);color:var(--white);font-size:11px;letter-spacing:1px;display:flex;align-items:center;justify-content:center}

/* featured */
.prod{width:205px;text-align:center}
.prod .img{width:205px;height:204px;background:var(--soft)}
.prod h3{font-weight:400;font-size:12px;line-height:18px;margin-top:22px;height:36px}
.prod .price{color:var(--gold);font-size:13px;margin-top:12px}
.prod .buy{width:128px;height:30px;margin:20px auto 0;color:var(--gold);font-size:10px;letter-spacing:1px;border-bottom:1px solid var(--line);display:flex;align-items:center;justify-content:center}
.prod .buy.on{background:var(--gold);color:var(--white);border:none}
.arrow{color:#bdbdbd;font-size:26px}

/* about */
.about{top:2636px;height:563px;background:linear-gradient(90deg,#5d5a58 0%,#8a8481 45%,#5f5c5b 100%)}
.about-kicker{left:611px;top:2770px;color:var(--white);font-size:18px;letter-spacing:1px}
.about-name{left:611px;top:2802px;color:var(--white);font-size:42px;line-height:1}
.about-text{left:611px;top:2878px;width:360px;color:var(--white);font-size:12.5px;line-height:19.5px}
.about-link{left:611px;top:3050px;width:130px;color:var(--white);font-size:11px;letter-spacing:1px;padding:8px 0 8px 28px;border-top:1px solid rgba(255,255,255,.6);border-bottom:1px solid rgba(255,255,255,.6)}

/* accent + quote */
.accent{left:154px;top:3279px;width:510px;height:402px;background:linear-gradient(90deg,#f1f1f3 0%,#eeeef0 45%,#c9c3c2 100%)}
.accent-title{left:229px;top:3404px;font-size:28px;line-height:35px;letter-spacing:1px;font-weight:400}
.accent-btn{left:229px;top:3570px;width:170px;height:28px;border:1px solid #bdbdbd;font-size:11px;letter-spacing:1px;display:flex;align-items:center;justify-content:center}
.quote{left:688px;top:3279px;width:358px;height:402px;background:var(--panel);text-align:center;color:var(--white)}
.quote .mark{color:var(--gold);font-size:34px;margin-top:70px;font-family:"Limelight",serif}
.quote p{font-family:"Cormorant Garamond",serif;font-size:17px;line-height:21px;width:200px;margin:12px auto 0}
.quote .chunk{color:var(--gold);font-size:11px;letter-spacing:1px;margin:38px auto 0;width:130px;padding-bottom:8px;border-bottom:1px solid #4a4444}

/* gallery */
.follow{left:150px;top:3766px;color:var(--gold);font-size:34px;font-weight:300;letter-spacing:1px}
.follow .name-mark{font-size:34px}
.insta-btn{left:802px;top:3765px;width:244px;height:32px;border-top:1px solid var(--line);border-bottom:1px solid var(--line);font-size:11px;letter-spacing:1px;display:flex;align-items:center;justify-content:center}
.insta{top:3877px;height:240px;display:flex}
.insta div{width:240px;height:240px}

/* newsletter + map */
.news{left:154px;top:4198px;width:433px;height:240px;background:var(--panel);color:var(--white)}
.news h4{position:absolute;left:75px;top:80px;font-weight:400;font-size:17px;letter-spacing:.5px}
.news .field{position:absolute;left:75px;top:122px;width:281px;height:38px;border:1px solid #6d6767;font-size:12px;color:#9a9494;display:flex;align-items:center;justify-content:space-between;padding:0 14px}
.map{left:613px;top:4198px;width:433px;height:240px;background:linear-gradient(135deg,#ecebe8,#e2e1dd)}

/* contact */
.contact{width:240px;text-align:center;top:4516px}
.contact .rule{height:1px;background:var(--line);margin:12px 0 16px}
.contact p{font-size:12px;line-height:15px;white-space:nowrap}

/* footer */
.site-foot{top:4708px;height:123px;background:var(--soft)}
.legal{left:154px;top:4752px;font-size:11px;line-height:19px;letter-spacing:.5px;color:var(--muted)}
.legal b{color:var(--gold);font-weight:400}
.social{left:887px;top:4752px;display:flex;gap:9px}
.social i{display:block;width:32px;height:32px;border-radius:50%;background:#8a8a8a}
.social i.on{background:var(--gold)}
</style>
</head>
<body>

<header class="hero">
  <div class="photo" role="img" aria-label="Close-up of a hand wearing a diamond solitaire engagement ring on soft fabric" style="inset:0"></div>
  <div class="abs brand"><div class="name name-mark">BRILL'S</div><div class="tag">YOUR HOMETOWN JEWELER</div></div>
  <nav class="abs nav">
    <span class="active">HOME</span><span>JEWELRY</span><span>SERVICES</span><span>ABOUT US</span><span>CONTACT</span><span>CALL &nbsp;(555) 010-0182</span>
  </nav>
  <div class="abs cart">
    <svg width="12" height="11" viewBox="0 0 12 11" fill="none" stroke="#fff" stroke-width="1.2"><path d="M0 1h2l1.5 6h7l1-4.5H3"/><circle cx="4.5" cy="9.5" r="1"/><circle cx="9.5" cy="9.5" r="1"/></svg>
    CART (0)
  </div>
  <h1 class="abs hero-title deco">YOUR PERFECT<br>STYLE</h1>
  <div class="abs hero-link">SHOP NOW</div>
  <div class="abs dots"><i></i><i></i><i></i></div>
</header>

<section class="services">
  <h2 class="abs sec-title" style="top:74px">OUR SERVICES</h2>
  <div class="abs svc" style="left:174px;top:140px">
    <svg width="60" height="60" viewBox="0 0 60 60" fill="none" stroke="#d6962b" stroke-width="1.8"><path d="M14 20h32l6 8-22 24L8 28z"/><path d="M8 28h44M22 20l-4 8 12 24 12-24-4-8"/><path d="M30 4v8M18 8l4 6M42 8l-4 6"/></svg>
    <div class="rule"></div><p>Appraisals</p>
  </div>
  <div class="abs svc" style="left:480px;top:140px">
    <svg width="60" height="60" viewBox="0 0 60 60" fill="none" stroke="#d6962b" stroke-width="1.8"><path d="M30 6l22 10v26L30 54 8 42V16z"/><path d="M8 16l22 10 22-10M30 26v28M19 11l22 10"/></svg>
    <div class="rule"></div><p>Consignment</p>
  </div>
  <div class="abs svc" style="left:786px;top:140px">
    <svg width="60" height="60" viewBox="0 0 60 60" fill="none" stroke="#d6962b" stroke-width="1.8"><path d="M12 8l10 10-4 4L8 12zM20 20l22 22M40 40l6 10 4-4-10-6"/><path d="M48 8a8 8 0 0 0-10 10L16 40a5 5 0 1 0 4 4l22-22a8 8 0 0 0 10-10l-5 4-4-1-1-4z"/></svg>
    <div class="rule"></div><p>Repairs</p>
  </div>
</section>

<section style="top:975px;height:688px">
  <h2 class="abs sec-title" style="top:77px">SHOP FOR JEWELRY</h2>
</section>
<div class="photo tile" role="img" aria-label="Rings on a hand" style="left:154px;top:1119px;background:linear-gradient(135deg,#cfc8c2,#8e857f)"></div>
<div class="photo tile" role="img" aria-label="Bracelet on a wrist" style="left:383px;top:1119px;background:linear-gradient(135deg,#e6e2de,#a69d98)"></div>
<div class="photo tile" role="img" aria-label="Earrings" style="left:611px;top:1119px;background:linear-gradient(135deg,#d9d3cf,#6e6662)"></div>
<div class="photo tile" role="img" aria-label="Necklaces on display" style="left:842px;top:1119px;background:linear-gradient(135deg,#6a7f3f,#2a3a6a)"></div>
<div class="abs tile-label" style="left:154px;top:1302px">Rings<span></span></div>
<div class="abs tile-label" style="left:383px;top:1302px">Bracelets<span></span></div>
<div class="abs tile-label on" style="left:611px;top:1302px">Earrings<span></span></div>
<div class="abs tile-label" style="left:842px;top:1302px">Necklaces<span></span></div>
<div class="photo tile" role="img" aria-label="Estate gold jewelry" style="left:154px;top:1367px;background:linear-gradient(135deg,#3a2410,#b57b2c)"></div>
<div class="photo tile" role="img" aria-label="Wrist watch" style="left:383px;top:1367px;background:linear-gradient(135deg,#2f3542,#6b4a3a)"></div>
<div class="photo tile" role="img" aria-label="Men's ring on dark stone" style="left:611px;top:1367px;background:linear-gradient(135deg,#3c3e42,#1c1d20)"></div>
<div class="photo tile" role="img" aria-label="Children's bracelet" style="left:842px;top:1367px;background:linear-gradient(135deg,#ece7e4,#cbbcb6)"></div>
<div class="abs tile-label" style="left:154px;top:1550px">Estate<span></span></div>
<div class="abs tile-label" style="left:383px;top:1550px">Watches<span></span></div>
<div class="abs tile-label" style="left:611px;top:1550px">Men's<span></span></div>
<div class="abs tile-label" style="left:842px;top:1550px">Children's<span></span></div>

<section class="banner">
  <div class="photo" role="img" aria-label="Pearl and diamond brooches on white wood" style="inset:0"></div>
</section>
<h2 class="abs banner-title deco"><span class="name-mark">BRILL'S</span> <span class="thin">FINE</span> JEWELRY<br><span class="thin">AND</span> DIAMONDS</h2>
<div class="abs btn-gold" style="left:154px;top:1931px;width:127px;height:34px">SHOP NOW</div>

<h2 class="abs sec-title" style="top:2140px">FEATURED PRODUCTS</h2>
<div class="abs arrow" style="left:94px;top:2296px">&#8249;</div>
<div class="abs arrow" style="left:1090px;top:2296px">&#8250;</div>
<div class="abs prod" style="left:154px;top:2207px">
  <div class="img" role="img" aria-label="Silver hoop oval earrings"></div>
  <h3>KNIFE EDGE HOOP OVAL<br>EARRINGS</h3><div class="price">$745</div><div class="buy">SHOP NOW</div>
</div>
<div class="abs prod" style="left:383px;top:2207px">
  <div class="img" role="img" aria-label="Pearl and diamond earrings"></div>
  <h3>ORNATE SILVER DIAMOND<br>EARRNINGS</h3><div class="price">$985</div><div class="buy on">SHOP NOW</div>
</div>
<div class="abs prod" style="left:611px;top:2207px">
  <div class="img" role="img" aria-label="Heart-shaped diamond stud earrings"></div>
  <h3>MODERN HEART-SHAPED<br>EARRINGS</h3><div class="price">$465</div><div class="buy">SHOP NOW</div>
</div>
<div class="abs prod" style="left:842px;top:2207px">
  <div class="img" role="img" aria-label="Gold pendant diamond setting"></div>
  <h3>PENDANT DIAMOND<br>SETTING</h3><div class="price">$1,125</div><div class="buy">SHOP NOW</div>
</div>

<section class="about">
  <div class="photo" role="img" aria-label="Hand wearing a pink gemstone ring" style="inset:0"></div>
</section>
<div class="abs about-kicker">ABOUT</div>
<div class="abs about-name name-mark">BRILL'S</div>
<p class="abs about-text">Sed ut perspiciatis unde omnis iste natus error sit voluptatem accusantium doloremque laudantium, totam rem aperiam, eaque ipsa quae ab illo inventore veritatis et quasi architecto beatae vitae dicta sunt explicabo. Nemo enim ipsam voluptatem quia voluptas sit aspernatur aut odit aut fugit, sed quia consequuntur magni dolores eos qui ratione voluptatem.</p>
<div class="abs about-link">READ MORE</div>

<div class="photo accent" role="img" aria-label="Statement necklace and red hat in soft light"></div>
<h2 class="abs accent-title">ACCENT<br>YOUR STYLE WITH<br>NEW<br>COLLECTION</h2>
<div class="abs accent-btn">NEW COLLECTION</div>
<div class="abs quote">
  <div class="mark">66</div>
  <p>Lorem ipsum dolor sit amet, consectetur adipiscing elit, sed do eiusmod tempor incididunt ut labore et dolore magna aliqua. Ut enim minim veniam, quis nostrud ...</p>
  <div class="chunk">STANDARD CHUNK</div>
</div>

<h2 class="abs follow">FOLLOW ON GALLERY <span class="name-mark">BRILL'S</span></h2>
<div class="abs insta-btn">VISIT GALLERY PAGE</div>
<section class="insta">
  <div role="img" aria-label="Gold bib necklace on a bust" style="background:linear-gradient(135deg,#c9a45a,#7a5a24)"></div>
  <div role="img" aria-label="Men's watch with leather strap" style="background:linear-gradient(135deg,#a9a39c,#3d2a22)"></div>
  <div role="img" aria-label="Storefront of the jewelry shop" style="background:linear-gradient(135deg,#3a3530,#8a7a66)"></div>
  <div role="img" aria-label="Butterfly pendant on a gold chain" style="background:linear-gradient(135deg,#e9c66a,#c9974a)"></div>
  <div role="img" aria-label="Diamond ring on display" style="background:linear-gradient(135deg,#ddd9d4,#8c8884)"></div>
</section>

<div class="abs news">
  <h4>NEWSLETTER SIGN UP!</h4>
  <div class="field">name@email.com
    <svg width="14" height="14" viewBox="0 0 14 14" fill="none" stroke="#fff" stroke-width="1.2"><path d="M1 6l12-5-5 12-2-5z"/></svg>
  </div>
</div>
<div class="photo map" role="img" aria-label="Street map showing the store location"></div>

<div class="abs contact" style="left:174px">
  <svg width="44" height="44" viewBox="0 0 44 44" fill="none" stroke="#d6962b" stroke-width="1.8"><path d="M10 6l7 7-4 5c3 6 7 10 13 13l5-4 7 7-5 5C20 38 6 24 5 11z"/></svg>
  <div class="rule"></div><p>(555)010-0182<br>HELLO@BRILLS-EXAMPLE.COM</p>
</div>
<div class="abs contact" style="left:476px">
  <svg width="44" height="44" viewBox="0 0 44 44" fill="none" stroke="#d6962b" stroke-width="1.8"><path d="M22 40S8 25 8 17a14 14 0 0 1 28 0c0 8-14 23-14 23z"/><circle cx="22" cy="17" r="5"/></svg>
  <div class="rule"></div><p>418 HARBOR LANE, PALM VISTA,<br>FL 39010</p>
</div>
<div class="abs contact" style="left:786px">
  <svg width="44" height="44" viewBox="0 0 44 44" fill="none" stroke="#d6962b" stroke-width="1.8"><rect x="6" y="9" width="32" height="29"/><path d="M6 17h32M14 5v8M30 5v8"/><circle cx="22" cy="28" r="6"/><path d="M22 25v3h3"/></svg>
  <div class="rule"></div><p>MON TO FRI: 10 - 6PM<br>SAT: 10AM - 3PM</p>
</div>

<footer class="site-foot"></footer>
<div class="abs legal">© 2020 <b>BRILL'S</b>. ALL RIGHTS RESERVED.<br>TERMS OF USE &nbsp;|&nbsp; PRIVACY POLICY</div>
<div class="abs social">
  <i aria-label="Social link 1"></i><i class="on" aria-label="Social link 2"></i><i aria-label="Social link 3"></i><i aria-label="Social link 4"></i>
</div>

</body>
</html>
```